KTV Business Card

Create a Simple but Elegant business card for a Luxury Off Road Vehicle and Accessories sales Company. Center of Letters we usually fill with red or a carbon fiber we don't want to limit creativity so anything goes. I think we would prefer large logo on the front and a smaller logo with infused QR reader on the back.
Some Ideas to get you heading more in the right direction are to put them on a thicker cardstock with red edges and we would need our logo letter (KTV) filled in with red. Example is the Vantorelli card in our brief. For the side with our info on it we are looking for our logo to include an embedded QR reader also in our brief.
Information to include 2 bullet points: Luxury Off Road Vehicle Sales / Custom Off Road Bumpers
Address:518 Pelling Road, Suite 164, The Woodlands, Texas
Phone# 555-318-0467,
Website: WWW.KTV-TRAILGEAR.EXAMPLE
Facebook: facebook.com/KTVTrailGear
Instagram: instagram.com/ktv_trailgear
Target Market(s)
Exotic Vehicle and Outdoor enthusiasts.
Industry/Entity Type
Business
Look and feel

```html
<!DOCTYPE html>
<html lang="en">
<head>
<meta charset="utf-8">
<title>KTV Business Card</title>
<link rel="stylesheet" href="https://fonts.googleapis.com/css2?family=Montserrat:wght@300;400;500;800&display=swap">
<style>
  :root {
    --backdrop: #e9e4dc;
    --card: #ffffff;
    --ink: #3a3838;
    --ink-soft: #555353;
    --red: #c8202a;
    --green: #9fcf6e;
    --green-deep: #7fb64c;
    --grey-band: #c9c9c9;
    --mark-light: rgba(255,255,255,0.55);
  }
  * { box-sizing: border-box; margin: 0; padding: 0; }
  html, body { width: 1200px; height: 1000px; overflow: hidden; }
  body {
    background: var(--backdrop);
    font-family: "Montserrat", sans-serif;
    position: relative;
  }
  .card {
    position: absolute;
    width: 620px;
    height: 354px;
    background: var(--card);
    border: 4px solid var(--red);
    border-radius: 4px;
    box-shadow: 0 10px 26px rgba(0,0,0,0.18);
    overflow: hidden;
  }
  .card--info { left: 50px; top: 110px; }
  .card--brand { left: 530px; top: 536px; }

  .card__bands { position: absolute; inset: 0; width: 100%; height: 100%; }

  .wordmark {
    position: absolute;
    display: flex;
    align-items: center;
    gap: 12px;
    color: var(--red);
    font-weight: 800;
    line-height: 1;
  }
  .qr-slot { background: var(--ink); flex: none; }
  .card--info .wordmark { right: 32px; top: 24px; font-size: 42px; }
  .card--info .qr-slot { width: 44px; height: 44px; }

  .holder-name {
    position: absolute;
    left: 0; right: 0;
    top: 118px;
    text-align: center;
    font-size: 36px;
    font-weight: 500;
    color: var(--ink);
    letter-spacing: -0.5px;
  }
  .services {
    position: absolute;
    left: 0; right: 0;
    top: 176px;
    display: flex;
    justify-content: center;
    gap: 22px;
    list-style: none;
    font-size: 13px;
    font-weight: 500;
    color: var(--ink-soft);
  }
  .services li::before { content: "• "; color: var(--red); }

  .contact-grid {
    position: absolute;
    left: 30px; right: 20px;
    top: 256px;
    display: grid;
    grid-template-columns: 280px 1fr;
    column-gap: 10px;
    font-size: 13px;
    font-weight: 400;
    color: var(--ink-soft);
    line-height: 20px;
  }
  .contact-list { list-style: none; }
  .contact-list li { display: flex; align-items: center; gap: 7px; white-space: nowrap; }
  .contact-list li.continued { padding-left: 19px; }
  .contact-list svg { width: 12px; height: 12px; flex: none; }

  .card--brand .wordmark {
    left: 56px; top: 56px;
    font-size: 150px;
    letter-spacing: 6px;
    gap: 26px;
  }
  .card--brand .qr-slot { width: 110px; height: 110px; }
  .brand-services {
    position: absolute;
    left: 62px; top: 228px;
    font-size: 16px;
    font-weight: 500;
    color: var(--ink-soft);
    letter-spacing: 0.5px;
  }
  .web-address {
    position: absolute;
    left: 62px; top: 272px;
    font-size: 22px;
    font-weight: 500;
    color: var(--ink);
  }
</style>
</head>
<body>

  <section class="card card--info" aria-label="Business card, contact side">
    <svg class="card__bands" viewBox="0 0 612 346" preserveAspectRatio="none" aria-hidden="true">
      <polygon points="0,40 70,40 150,96 612,96 612,106 140,106 60,158 0,158" fill="var(--green)"/>
      <circle cx="58" cy="99" r="32" fill="var(--mark-light)"/>
      <polygon points="0,220 466,220 516,186 612,186 612,248 536,248 486,230 0,230" fill="var(--grey-band)"/>
      <circle cx="566" cy="217" r="24" fill="var(--mark-light)"/>
    </svg>

    <div class="wordmark"><span>KTV</span><span class="qr-slot" role="img" aria-label="QR code area"></span></div>

    <h1 class="holder-name">John Doe</h1>

    <ul class="services">
      <li>Luxury Off Road Vehicle Sales</li>
      <li>Custom Off Road Bumpers</li>
    </ul>

    <div class="contact-grid">
      <ul class="contact-list">
        <li>
          <svg viewBox="0 0 16 16"><path d="M4 1l3 3-2 2c1 2 3 4 5 5l2-2 3 3-2 3C7 15 1 9 1 3z" fill="var(--green-deep)"/></svg>
          555-318-0467
        </li>
        <li>
          <svg viewBox="0 0 16 16"><path d="M8 1a5 5 0 0 1 5 5c0 4-5 9-5 9S3 10 3 6a5 5 0 0 1 5-5z" fill="var(--green-deep)"/><circle cx="8" cy="6" r="2" fill="#fff"/></svg>
          518 Pelling Road, Suite 164
        </li>
        <li class="continued">The Woodlands, Texas</li>
      </ul>
      <ul class="contact-list">
        <li>
          <svg viewBox="0 0 16 16"><circle cx="8" cy="8" r="6.5" fill="none" stroke="var(--green-deep)" stroke-width="2"/></svg>
          WWW.KTV-TRAILGEAR.EXAMPLE
        </li>
        <li>
          <svg viewBox="0 0 16 16"><rect x="1" y="3" width="14" height="10" fill="var(--green-deep)"/><path d="M1 3l7 6 7-6" fill="none" stroke="#fff" stroke-width="1.5"/></svg>
          info@ktv-trailgear.example
        </li>
        <li>
          <svg viewBox="0 0 16 16"><rect x="2" y="2" width="12" height="12" fill="var(--green-deep)"/></svg>
          facebook.com/KTVTrailGear
        </li>
        <li>
          <svg viewBox="0 0 16 16"><rect x="2" y="2" width="12" height="12" fill="none" stroke="var(--green-deep)" stroke-width="2"/></svg>
          instagram.com/ktv_trailgear
        </li>
      </ul>
    </div>
  </section>

  <section class="card card--brand" aria-label="Business card, brand side">
    <div class="wordmark"><span>KTV</span><span class="qr-slot" role="img" aria-label="QR code area"></span></div>
    <p class="brand-services">Luxury Off Road Vehicle Sales · Custom Off Road Bumpers</p>
    <p class="web-address">WWW.KTV-TRAILGEAR.EXAMPLE</p>
  </section>

</body>
</html>
```